Have Logo - Need Business Card Design!!!

I am looking for a business card design for a real estate development business. The company name is Orvane Realty Partners. I already have a logo created by Pixel Harbor and would like this logo to be incorporated into the design. I have uploaded the files. The card needs to be professional, but visually interesting. Not necessary to be double-sided, but if you want to get creative and can think of something to put on the back then have at it.

Target Market(s)

The target audience for these business cards will be professionals in the real estate industry.

Industry/Entity Type

Real Estate

Requirements
Must have
• The business card must have all the necessary items for a business card, i.e. company name, our logo, name (however, not title necessary), office address, office phone number, cell number, fax number, website address, etc.

You can use the information below for the card:

Martin R. Oswell
812 Linden Avenue
San Francisco, California 94177

www.orvanerealtypartners.example
moswell@orvanerealtypartners.example
Office: 415-555-0143
Fax: 415-555-0147
Cell: 415-555-0182

```html
<!DOCTYPE html>
<html lang="en">
<head>
<meta charset="utf-8">
<title>Orvane Realty Partners – Business Card</title>
<link rel="stylesheet" href="https://fonts.googleapis.com/css2?family=Arimo:wght@400;700&display=swap">
<style>
  :root {
    --canvas-bg: #e6e6e6;
    --brand-green: #1a8a42;
    --brand-green-deep: #137536;
    --card-white: #ffffff;
    --card-grey-light: #ececec;
    --band-grey: #a3a5a7;
    --band-divider: #d7d8d9;
    --text-light: #ffffff;
  }
  * { box-sizing: border-box; margin: 0; padding: 0; }
  html, body {
    width: 1200px;
    height: 951px;
    overflow: hidden;
  }
  body {
    background: var(--canvas-bg);
    font-family: "Arimo", Arial, sans-serif;
    position: relative;
  }
  .card {
    position: absolute;
    width: 560px;
    height: 320px;
    border-radius: 22px;
    overflow: hidden;
    box-shadow: 0 6px 18px rgba(0,0,0,0.18);
  }

  /* Front side */
  .card-front {
    left: 70px;
    top: 90px;
    background: radial-gradient(ellipse at 45% 40%, var(--brand-green) 0%, var(--brand-green-deep) 100%);
    color: var(--text-light);
  }
  .company-name {
    position: absolute;
    left: 0;
    right: 0;
    top: 128px;
    text-align: center;
    font-size: 38px;
    font-weight: 400;
    line-height: 1;
    color: var(--text-light);
  }
  .website {
    position: absolute;
    left: 0;
    right: 0;
    top: 236px;
    text-align: center;
    font-size: 15px;
    font-weight: 400;
    letter-spacing: 0.3px;
  }

  /* Back side */
  .card-back {
    left: 570px;
    top: 520px;
    background: linear-gradient(180deg, var(--card-white) 0%, var(--card-grey-light) 100%);
  }
  .contact-band {
    position: absolute;
    left: 0;
    right: 0;
    top: 92px;
    height: 152px;
    display: flex;
  }
  .name-panel {
    width: 228px;
    background: var(--brand-green);
    color: var(--text-light);
    display: flex;
    align-items: center;
    justify-content: center;
    font-size: 18px;
    letter-spacing: 0.5px;
  }
  .details-panel {
    flex: 1;
    background: var(--band-grey);
    color: var(--text-light);
    padding: 10px 0 0 22px;
    position: relative;
    font-size: 14px;
    line-height: 19px;
    letter-spacing: 0.3px;
  }
  .details-panel::before {
    content: "";
    position: absolute;
    left: 8px;
    top: 14px;
    bottom: 14px;
    width: 1px;
    background: var(--band-divider);
  }
  .address { margin-bottom: 10px; }
</style>
</head>
<body>
  <section class="card card-front" aria-label="Card front">
    <p class="company-name">Orvane Realty Partners</p>
    <p class="website">www.orvanerealtypartners.example</p>
  </section>

  <section class="card card-back" aria-label="Card back">
    <div class="contact-band">
      <div class="name-panel">Martin R. Oswell</div>
      <div class="details-panel">
        <p class="address">812 Linden Avenue<br>San Francisco, California 94177</p>
        <p class="phones">Office: 415-555-0143<br>Fax: 415-555-0147<br>Cell: 415-555-0182</p>
        <p class="email">moswell@orvanerealtypartners.example</p>
      </div>
    </div>
  </section>
</body>
</html>
```